Flyer Tally Desk Ledger Kit

Hi
Can you please design me a DL Flyer for: Tally Desk Ledger Kit
Info:
Starting a new Business ?
Want to save on bookkeeping fees for your existing business?

You can now save 1000's off bookkeeping fees by Doing it Yourself.

Using our Bookkeeper software you simply key in the information as you go.

We offer one on one training, backup and support.
We can assist you with BAS Preparation and Payrol Advice.

Add Modules as required:
Point of Sale Module
Jobs Management Module
Website Intergration Module

Fee set up assistance and training.

Lets get the ball rolling: 1300 462 815
www.tldlk.com.au
admin@tldlk.com.au (use the logo thing you made)

Target Market(s)

Small Business

Colors
ec1f27
f04a50
f59296
fcdcdc
ffffff

Requirements
Nice to have
• image/s related to bookkeeping

```html
<!DOCTYPE html>
<html lang="en">
<head>
<meta charset="utf-8">
<title>Tally Desk Ledger Kit – DL Flyer</title>
<link href="https://fonts.googleapis.com/css2?family=Bebas+Neue&family=Source+Sans+3:wght@400;600&display=swap" rel="stylesheet">
<style>
  :root {
    --red: #ec1f27;
    --red-soft: #f04a50;
    --pink: #f59296;
    --blush: #fcdcdc;
    --white: #ffffff;
    --slate: #3d3e40;
  }
  * { margin: 0; padding: 0; box-sizing: border-box; }
  html, body { width: 1200px; height: 2546px; overflow: hidden; background: var(--white); }
  .flyer { position: relative; width: 1200px; height: 2546px; overflow: hidden; background: var(--white); }

  .headline-font { font-family: "Bebas Neue", "Oswald", sans-serif; color: var(--white); text-align: center; line-height: 1; }

  .top-band {
    position: absolute; left: 0; top: 0; width: 1200px; height: 172px;
    background: var(--red);
    display: flex; align-items: center; justify-content: center;
  }
  .top-band h1 { font-size: 132px; font-weight: 400; letter-spacing: 1px; padding-top: 8px; }

  .hero-art { position: absolute; left: 0; top: 172px; width: 1200px; height: 1520px; }

  .hero-copy { position: absolute; left: 0; width: 1200px; }
  .hero-copy .big { position: absolute; top: 815px; width: 100%; font-size: 168px; }
  .hero-copy .line { position: absolute; width: 100%; font-size: 92px; }
  .hero-copy .l1 { top: 990px; }
  .hero-copy .l2 { top: 1103px; }

  .savings { position: absolute; left: 0; top: 1485px; width: 1200px; }
  .savings p { font-size: 88px; }
  .savings p + p { margin-top: 10px; }

  .features {
    position: absolute; left: 80px; top: 1742px; width: 1041px; height: 436px;
    background: var(--slate); border-radius: 52px;
    padding: 52px 40px 0 30px;
    list-style: none;
    font-family: "Source Sans 3", "Myriad Pro", sans-serif; font-weight: 400;
    color: var(--white); font-size: 44px; line-height: 51px;
  }
  .features li { position: relative; padding-left: 140px; text-indent: -0px; margin-bottom: 26px; }
  .features li::before {
    content: ""; position: absolute; left: 80px; top: 12px;
    width: 34px; height: 34px; border-radius: 50%; background: var(--white);
  }
  .features li { padding-left: 140px; margin-left: -80px; }

  .footer-band {
    position: absolute; left: 0; top: 2227px; width: 1200px; height: 319px;
    background: var(--red);
    display: flex; flex-direction: column; align-items: center; justify-content: center;
    font-family: "Source Sans 3", "Myriad Pro", sans-serif; color: var(--white);
  }
  .brand { display: flex; align-items: center; gap: 30px; }
  .brand-dot { width: 64px; height: 64px; border-radius: 50%; background: var(--white); }
  .brand-name { font-size: 92px; font-weight: 600; line-height: 1; letter-spacing: -1px; }
  .tagline { margin-top: 22px; font-size: 44px; font-weight: 400; }
</style>
</head>
<body>
<main class="flyer">
  <header class="top-band">
    <h1 class="headline-font">Starting a new business ?</h1>
  </header>

  <svg class="hero-art" viewBox="0 172 1200 1520" width="1200" height="1520" aria-hidden="false">
    <defs>
      <linearGradient id="office-tones" x1="0" y1="0" x2="1" y2="1">
        <stop offset="0" stop-color="#b9a796"/>
        <stop offset="0.35" stop-color="#8c7a70"/>
        <stop offset="0.6" stop-color="#a2362f"/>
        <stop offset="1" stop-color="#6f6660"/>
      </linearGradient>
    </defs>
    <rect x="0" y="172" width="1200" height="1300" fill="url(#office-tones)" role="img" aria-label="Photo of a young woman in glasses and a red jumper working at a laptop in an office"/>
    <path d="M0,1100 C300,1400 700,1500 1200,1190 L1200,1692 L0,1692 Z" fill="var(--white)"/>
    <path d="M0,1195 C300,1430 760,1475 1200,1190 L1200,1692 L0,1692 Z" fill="var(--red)"/>
  </svg>

  <section class="hero-copy headline-font">
    <h2 class="big">Want to save</h2>
    <p class="line l1">On bookkeeping fees for your</p>
    <p class="line l2">existing business ?</p>
  </section>

  <section class="savings headline-font">
    <p>You can now save 1000’s off</p>
    <p>bookkeeping fees by doing it yourself</p>
  </section>

  <ul class="features">
    <li>Using our Bookkeeper software you simply key in the information as you go.</li>
    <li>We offer one on one training, backup and support.</li>
    <li>We can assist you with BAS Preparation and Payrol Advice.</li>
  </ul>

  <footer class="footer-band">
    <div class="brand">
      <span class="brand-dot"></span>
      <span class="brand-name">Tally Desk Ledger Kit</span>
    </div>
    <p class="tagline">It's easy enough to do yourself</p>
  </footer>
</main>
</body>
</html>
```